Wirenexa

I'm looking to much improve our current website wirenexa.com
Updates

Low design quality

Target Market(s)

Commercial clients (Not-Residentials)

Industry/Entity Type

Office buildings and Industrial clients

Coding

Coded - Design and coding required

Number of Pages Required

5+ page

Requirements
Must have
• Very professional structured low voltage cabling projects for Wi-Fi, Audio/Video conference rooms, Access Control systems, CCTV.

```html
<!DOCTYPE html>
<html lang="en">
<head>
<meta charset="utf-8">
<title>Wirenexa – Structured Cabling & Low Voltage Experts</title>
<link href="https://fonts.googleapis.com/css2?family=Archivo:wght@600;700;800&family=Roboto:wght@400;500;700&display=swap" rel="stylesheet">
<style>
:root{
  --red:#d42a1e;
  --black:#000;
  --ink:#111;
  --text:#555;
  --light:#f2f2f2;
  --white:#fff;
  --dark:#1b1b1b;
}
*{box-sizing:border-box;margin:0;padding:0}
html,body{width:1200px;height:4167px;overflow:hidden}
body{position:relative;font-family:'Roboto',Arial,sans-serif;color:var(--ink);background:var(--white)}
.abs{position:absolute}
.head{font-family:'Archivo',Arial,sans-serif;font-weight:800;text-transform:uppercase;letter-spacing:-.5px}
.red{color:var(--red)}
.rule{position:absolute;height:4px;width:80px;background:var(--ink)}

/* top bar */
.topbar{left:0;top:0;width:1200px;height:50px;background:var(--black);color:#fff;font-size:11px;font-weight:700}
.topbar .item{position:absolute;top:18px;display:flex;align-items:center;gap:8px}
.social{position:absolute;top:17px;width:16px;height:16px;border-radius:50%;background:#fff}

/* nav */
.nav{left:0;top:50px;width:1200px;height:71px;background:#fff}
.logo{position:absolute;left:48px;top:20px;display:flex;align-items:center;gap:6px;font-family:'Archivo',sans-serif;font-weight:800;font-size:27px;color:var(--red)}
.logo .mark{width:22px;height:22px;background:var(--red)}
.nav a{position:absolute;top:29px;font-size:11.5px;color:var(--ink);text-decoration:none}
.nav a.active{color:var(--red)}
.survey{position:absolute;left:962px;top:20px;width:182px;height:32px;background:var(--red);transform:skewX(-15deg);color:#fff;font-size:11px;font-weight:700;display:flex;align-items:center;justify-content:center}
.survey span{transform:skewX(15deg)}

/* hero */
.hero{left:0;top:121px;width:1200px;height:518px;overflow:hidden}
.hero-photo{position:absolute;inset:0;background:linear-gradient(90deg,#222 0%,#3a3a3a 45%,#6b7079 60%,#8c8f94 100%)}
.hero h1{position:absolute;left:48px;top:60px;color:#fff;font-size:53px;line-height:65px}
.hero p{position:absolute;left:48px;top:278px;color:#fff;font-size:14px;line-height:27px;width:460px}
.btn-outline{position:absolute;border:1.5px solid var(--red);display:flex;align-items:center;justify-content:center;font-size:11px;font-weight:700;color:#fff}
.hero .btn-outline{left:56px;top:372px;width:150px;height:41px;transform:skewX(-15deg)}
.hero .btn-outline span{transform:skewX(15deg)}

/* about */
.about h2{position:absolute;left:48px;top:748px;font-size:46px}
.about .lead{position:absolute;left:48px;top:858px;width:400px;font-size:14px;line-height:27px;color:var(--ink)}
.about .body{position:absolute;left:48px;top:940px;width:405px;font-size:14px;line-height:27px;color:var(--text)}
.about .btn{position:absolute;left:48px;top:1135px;width:144px;height:44px;border:1.5px solid var(--red);color:var(--ink);font-size:14px;display:flex;align-items:center;justify-content:center}
.ph{position:absolute}

/* services */
.sec-title{position:absolute;left:0;width:1200px;text-align:center;font-size:44px}
.svc h3{position:absolute;font-family:'Archivo',sans-serif;font-weight:700;font-size:26px;text-transform:uppercase}
.svc p{position:absolute;width:530px;font-size:14px;line-height:27px;color:var(--text)}

/* promises */
.promises{left:0;top:2013px;width:1200px;height:566px;background:var(--light)}
.prom{position:absolute;width:380px}
.prom h4{font-family:'Roboto',sans-serif;font-weight:700;font-size:16px;text-transform:uppercase;margin-bottom:10px}
.prom p{font-size:11px;line-height:18px;color:var(--text)}
.prom.left{text-align:right}
.ic{position:absolute;width:56px;height:56px;border-radius:50%;background:var(--black);border:3px solid #fff;box-shadow:0 0 0 1px #ccc;display:flex;align-items:center;justify-content:center}
.ic.r{background:var(--red)}

/* testimonials */
.testi{left:0;top:2579px;width:1200px;height:469px;background:linear-gradient(180deg,#151515,#262626 50%,#1a1a1a)}
.card{position:absolute;top:181px;width:356px;height:180px;background:#f4f4f4;border-radius:12px}
.card .name{position:absolute;left:62px;top:26px;font-size:12px;font-weight:700}
.card .stars{position:absolute;left:160px;top:20px;color:var(--red);font-size:18px;letter-spacing:3px}
.card p{position:absolute;left:62px;top:58px;width:270px;font-size:12.5px;line-height:27px;color:var(--text)}
.avatar{position:absolute;top:-18px;left:-12px;width:60px;height:60px;border-radius:50%;background:linear-gradient(135deg,#6b5846,#2b231c)}
.dot{position:absolute;top:411px;width:15px;height:15px;border-radius:50%;background:#ddd}

/* footer */
.footer{left:0;top:3700px;width:1200px;height:467px;background:var(--black);color:#fff}
.footer h3{position:absolute;left:48px;top:76px;font-size:27px;line-height:34px}
.crow{position:absolute;left:48px;display:flex;gap:14px;align-items:flex-start;font-size:11px;line-height:15px}
.crow .pin{width:38px;height:38px;border-radius:50%;background:#fff;display:flex;align-items:center;justify-content:center;flex:none}
.crow b{font-weight:700;font-size:12px}
.form{position:absolute;left:522px;top:64px;width:531px;height:338px;border:2px solid var(--red)}
.form h3{position:absolute;left:34px;top:18px;font-size:26px;line-height:32px}
.form label{position:absolute;font-size:12px}
.form .field{position:absolute;width:217px;height:32px;border:1px solid #aaa}
.form .send{position:absolute;left:274px;top:242px;width:217px;height:42px;border:2px solid var(--red);color:#fff;font-size:14px;display:flex;align-items:center;justify-content:center}
.copy-line{position:absolute;left:48px;top:431px;width:1104px;height:1px;background:#555}
.copy{position:absolute;left:0;top:442px;width:1200px;text-align:center;font-size:11px}
</style>
</head>
<body>

<header class="abs topbar">
  <div class="item" style="left:50px">
    <svg width="16" height="12" viewBox="0 0 16 12"><rect width="16" height="12" rx="1" fill="#fff"/><path d="M1 1l7 6 7-6" stroke="#000" stroke-width="1.5" fill="none"/></svg>
    EMAIL: info@wirenexa.com
  </div>
  <div class="item" style="left:278px">
    <svg width="14" height="14" viewBox="0 0 24 24"><path fill="#fff" d="M6.6 10.8a15 15 0 006.6 6.6l2.2-2.2c.3-.3.7-.4 1-.2 1.1.4 2.3.6 3.6.6.6 0 1 .4 1 1V20c0 .6-.4 1-1 1A17 17 0 013 4c0-.6.4-1 1-1h3.5c.6 0 1 .4 1 1 0 1.3.2 2.5.6 3.6.1.3 0 .7-.2 1z"/></svg>
    GENREL ENQUIRIES:(800)-555-0147
  </div>
  <span class="social" style="left:1009px"></span>
  <span class="social" style="left:1046px"></span>
  <span class="social" style="left:1090px"></span>
  <span class="social" style="left:1132px"></span>
</header>

<nav class="abs nav">
  <div class="logo"><span class="mark"></span>Wirenexa</div>
  <a class="active" style="left:325px">HOME</a>
  <a style="left:414px">ABOUT</a>
  <a style="left:506px">SERVICES</a>
  <a style="left:614px">INDUSTRIES</a>
  <a style="left:734px">PROJECTS</a>
  <a style="left:846px">CONTACT</a>
  <div class="survey"><span>SCHEDULE SITE SURVEY ➚</span></div>
</nav>

<section class="abs hero">
  <div class="hero-photo" role="img" aria-label="Technician in a hard hat and safety glasses wiring a network panel"></div>
  <h1 class="head">Structured<br>Cabling &amp; Low<br>Voltage Experts</h1>
  <p>Professional CAT6, Fiber Optic, Wi-Fi, Security &amp; Data Infrastructure Solutions For Commercial And Industrial Facilities.</p>
  <div class="btn-outline"><span>REQUEST QUOTE ➚</span></div>
  <svg class="abs" style="left:0;top:0" width="1200" height="518" viewBox="0 0 1200 518">
    <path d="M0 498 C300 520 700 470 1200 455 L1200 518 L0 518Z" fill="#fff"/>
    <path d="M0 478 C300 508 700 462 1200 452 L1200 460 C700 472 300 522 0 500Z" fill="#d42a1e"/>
  </svg>
</section>

<section class="about">
  <h2 class="head">About <span class="red">Us</span></h2>
  <div class="rule" style="left:48px;top:818px;width:66px;height:3px"></div>
  <p class="lead">Elevate Your Connectivity With Wirenexa's Low Voltage Cabling Solutions</p>
  <p class="body">Wirenexa Is Your Premier Provider Of Professional Low Voltage Cabling Services In Virginia, Washington DC, And Maryland. With A Focus On Quality, Reliability, And Attention To Detail, We Deliver Exceptional Cabling Solutions For Audio, Video, Security Systems, Computer Networks, And More.</p>
  <div class="btn">LEARN MORE</div>
  <div class="ph" style="left:773px;top:721px;width:427px;height:506px;background:linear-gradient(135deg,#9a9ea3,#5a5f66 50%,#3c4048)" role="img" aria-label="Technician organising bundles of network cable in a wiring closet"></div>
  <div class="ph" style="left:538px;top:773px;width:330px;height:380px;background:linear-gradient(135deg,#ffffff,#ececec);box-shadow:0 4px 14px rgba(0,0,0,.25)" role="img" aria-label="Colourful thirty years anniversary emblem"></div>
</section>

<section class="svc">
  <h2 class="head sec-title" style="top:1338px">What We <span class="red">Do</span></h2>
  <div class="rule" style="left:560px;top:1406px"></div>
  <div class="ph" style="left:48px;top:1452px;width:528px;height:288px;background:linear-gradient(90deg,#e9e4dc,#b9a68c 55%,#efece7)" role="img" aria-label="Installer in a hard hat pulling cable coils through a ceiling"></div>
  <div class="ph" style="left:624px;top:1452px;width:527px;height:288px;background:linear-gradient(180deg,#6b7078,#9b9d9e 55%,#7a746c)" role="img" aria-label="Industrial site with underground conduit cables and a worker in hi-vis clothing"></div>
  <h3 style="left:48px;top:1758px">Commercial Services</h3>
  <h3 style="left:624px;top:1758px">Industrial Services</h3>
  <p style="left:48px;top:1805px">From Copper CAT6 And CAT7 Cabling To Fiber Optic Installations (Single And Multimode) And Wi-Fi Setup, We Offer A Full Range Of Low Voltage Cabling Services To Meet Your Specific Needs. Our Solutions Are Tailored To Your Requirements, Ensuring Seamless Connectivity And Optimal Performance.</p>
  <p style="left:624px;top:1805px">Whether You're A Commercial Business Or An Industrial Facility, We Have The Expertise And Resources To Support Your Cabling Needs. From Office Buildings To Data Centers, We Have The Capabilities To Handle Diverse Environments And Requirements.</p>
</section>

<section class="abs promises">
  <h2 class="head sec-title" style="top:58px"><span class="red">Our</span> Promises</h2>
  <div class="rule" style="left:560px;top:126px"></div>
  <div class="ph" style="left:453px;top:175px;width:294px;height:391px;background:linear-gradient(180deg,#c7cbce,#a4b3c4 55%,#7f9ec3)" role="img" aria-label="Smiling engineer wearing a white hard hat, shirt and red tie"></div>

  <div class="prom left" style="left:15px;top:232px"><h4>Structured Cabling</h4><p>CAT6/CAT6A Fiber Backbone<br>Rack BuildoutsCable Certification</p></div>
  <div class="prom left" style="left:15px;top:337px"><h4>Enterprise Wi-Fi</h4><p>Wireless SurveysAccess Point<br>Installation Large Facility Coverage Mesh / Cloud / Managed</p></div>
  <div class="prom left" style="left:15px;top:440px"><h4>Audio/Video Conference Rooms</h4><p>Video Rooms Huddle Rooms<br>Display Systems Integrated AVn Controls</p></div>

  <div class="prom" style="left:805px;top:241px"><h4>Access Control Systems</h4><p>Keycard Entry Door Controllers Biometric<br>Access Visitor Management</p></div>
  <div class="prom" style="left:807px;top:346px"><h4>CCTV &amp; Surveillance</h4><p>IP Camera Systems Remote MonitoringNVR<br>SolutionsCommercial Security</p></div>
  <div class="prom" style="left:807px;top:449px"><h4>MDF / IDF Infrastructure</h4><p>Rack Design Patch Panels UPS Systems<br>Cooling &amp; Organization</p></div>

  <div class="ic" style="left:417px;top:234px"><svg width="22" height="22" viewBox="0 0 24 24" fill="none" stroke="#fff" stroke-width="2"><rect x="6" y="3" width="8" height="18"/><path d="M14 7h4M14 12h4M14 17h4"/></svg></div>
  <div class="ic r" style="left:417px;top:339px"><svg width="22" height="22" viewBox="0 0 24 24" fill="none" stroke="#fff" stroke-width="2"><path d="M3 9a13 13 0 0118 0M6 13a8 8 0 0112 0M9 16.5a3.5 3.5 0 016 0"/><circle cx="12" cy="19.5" r="1" fill="#fff"/></svg></div>
  <div class="ic" style="left:417px;top:442px"><svg width="22" height="22" viewBox="0 0 24 24" fill="none" stroke="#fff" stroke-width="2"><rect x="6" y="3" width="12" height="18"/><path d="M10 7h4v6h-4z"/></svg></div>
  <div class="ic" style="left:726px;top:243px"><svg width="22" height="22" viewBox="0 0 24 24" fill="none" stroke="#fff" stroke-width="1.8"><circle cx="12" cy="12" r="9"/><circle cx="12" cy="12" r="5"/><path d="M12 9v5"/></svg></div>
  <div class="ic r" style="left:726px;top:348px"><svg width="22" height="22" viewBox="0 0 24 24" fill="none" stroke="#fff" stroke-width="2"><path d="M4 6l12 3-2 5-10-3z"/><path d="M8 13v5H4"/></svg></div>
  <div class="ic" style="left:726px;top:451px"><svg width="22" height="22" viewBox="0 0 24 24" fill="none" stroke="#fff" stroke-width="1.8"><circle cx="12" cy="12" r="9"/><circle cx="12" cy="12" r="2"/><path d="M12 10V4M14 12h6M12 14v6M10 12H4"/></svg></div>
</section>

<section class="abs testi" role="img" aria-label="Dark background photo of cable installation work">
  <h2 class="head sec-title" style="top:60px;color:#fff"><span class="red">Client</span> Testimonials</h2>
  <div class="rule" style="left:560px;top:126px;background:#fff"></div>
  <div class="card" style="left:48px"><span class="avatar"></span><span class="name">JHON SMITH</span><span class="stars">★★★★★</span><p>lorem ipsum dolor sit amet, consectetur adipiscing elit. vivamus in lectus malesuada, mollis libero a, ullamcorper metus. ut aliquet ex dui, eu accumsan nisi porttitor at.</p></div>
  <div class="card" style="left:422px"><span class="avatar"></span><span class="name">JHON SMITH</span><span class="stars">★★★★★</span><p>lorem ipsum dolor sit amet, consectetur adipiscing elit. vivamus in lectus malesuada, mollis libero a, ullamcorper metus. ut aliquet ex dui, eu accumsan nisi porttitor at.</p></div>
  <div class="card" style="left:797px"><span class="avatar"></span><span class="name">JHON SMITH</span><span class="stars">★★★★★</span><p>lorem ipsum dolor sit amet, consectetur adipiscing elit. vivamus in lectus malesuada, mollis libero a, ullamcorper metus. ut aliquet ex dui, eu accumsan nisi porttitor at.</p></div>
  <span class="dot" style="left:562px;background:var(--red)"></span>
  <span class="dot" style="left:582px"></span>
  <span class="dot" style="left:602px"></span>
  <span class="dot" style="left:622px"></span>
</section>

<section class="gallery">
  <h2 class="head sec-title" style="top:3150px;left:-16px"><span class="red">Our</span> Gallery</h2>
  <div class="rule" style="left:560px;top:3218px"></div>
  <div class="ph" style="left:48px;top:3253px;width:552px;height:347px;background:linear-gradient(90deg,#8a8f96,#5d6a7a 45%,#a7793f 80%,#3b3f46)" role="img" aria-label="Server room under construction with cable drums and blue conduit"></div>
  <div class="ph" style="left:600px;top:3253px;width:551px;height:347px;background:linear-gradient(90deg,#7c5d3c,#c9b497 50%,#e6e1d9)" role="img" aria-label="Two site engineers in hard hats reviewing a floor plan"></div>
</section>

<footer class="abs footer">
  <h3 class="head">Leave Your Enquiries And<br>We Will Contact You<br>Or Call 800-555-0147</h3>
  <div class="crow" style="top:212px">
    <span class="pin"><svg width="16" height="18" viewBox="0 0 24 24"><path fill="#000" d="M12 2a7 7 0 00-7 7c0 5 7 13 7 13s7-8 7-13a7 7 0 00-7-7zm0 9.5A2.5 2.5 0 1112 6.5a2.5 2.5 0 010 5z"/></svg></span>
    <div><b>Office Location</b><br>4410 Meridian Way, Suite 120<br>Fairview, VA 22000</div>
  </div>
  <div class="crow" style="top:274px">
    <span class="pin"><svg width="16" height="12" viewBox="0 0 16 12"><rect width="16" height="12" rx="1" fill="#000"/><path d="M1 1l7 6 7-6" stroke="#fff" stroke-width="1.5" fill="none"/></svg></span>
    <div><b>Email :</b><br>sales@wirenexa.com</div>
  </div>
  <div class="crow" style="top:336px">
    <span class="pin"><svg width="16" height="16" viewBox="0 0 24 24"><path fill="#000" d="M6.6 10.8a15 15 0 006.6 6.6l2.2-2.2c.3-.3.7-.4 1-.2 1.1.4 2.3.6 3.6.6.6 0 1 .4 1 1V20c0 .6-.4 1-1 1A17 17 0 013 4c0-.6.4-1 1-1h3.5c.6 0 1 .4 1 1 0 1.3.2 2.5.6 3.6.1.3 0 .7-.2 1z"/></svg></span>
    <div><b>Phone :</b><br>National:&nbsp;&nbsp;800-555-0147<br>Local:&nbsp;&nbsp;&nbsp;&nbsp;&nbsp;&nbsp;&nbsp;703-555-0182</div>
  </div>

  <div class="form">
    <h3 class="head">Request A Quote Today</h3>
    <label style="left:34px;top:74px">First Name</label>
    <label style="left:274px;top:74px">Last Name</label>
    <span class="field" style="left:34px;top:91px"></span>
    <span class="field" style="left:274px;top:91px"></span>
    <label style="left:34px;top:155px">Phone</label>
    <label style="left:274px;top:155px">Email</label>
    <span class="field" style="left:34px;top:172px"></span>
    <span class="field" style="left:274px;top:172px"></span>
    <label style="left:34px;top:238px">Message</label>
    <span class="field" style="left:34px;top:254px"></span>
    <div class="send">SEND MESSAGE</div>
  </div>

  <div class="copy-line"></div>
  <p class="copy">Copyright © 2026 Wirenexa Powered By Wirenexa</p>
</footer>

</body>
</html>
```